Clear Road Rentals flyer

Need a A6 size horizontal layout flyer. See attached example for ideas as well as some images I have which you can use. we are a hire car company that provides vehicles to clients who have recently been involved in car accidents and who's cars are currently getting fixed and so they lose the use of their own vehicle. see our website to keep flyer in line with website and for any further information clearroadrentals.com.au

Target Market(s)

people involved in not at fault car accidents

Industry/Entity Type

It Company

Requirements
Must have
• *ask people to let us know where they got our flyer from when they call us
• *call to action for people to call our phone number 1800 452 817
Should not have
• any mentioning that the vehicle is free

```html
<!DOCTYPE html>
<html lang="en">
<head>
<meta charset="utf-8">
<title>Clear Road Rentals Flyer</title>
<link rel="stylesheet" href="https://fonts.googleapis.com/css2?family=Lato:wght@400;700;900&display=swap">
<style>
  :root {
    --page: #e6e6e6;
    --paper: #ffffff;
    --ink: #222222;
    --blue: #3a97f5;
    --orange: #f58220;
    --panel: #dddddd;
    --muted: #555555;
    --light-text: #fff6e8;
    --photo-car-a: #8a8a84;
    --photo-car-b: #d9d9d6;
    --photo-people-a: #c9d3dc;
    --photo-people-b: #8c6f62;
  }
  * { margin: 0; padding: 0; box-sizing: border-box; }
  html, body { width: 1200px; height: 1200px; overflow: hidden; }
  body { background: var(--page); font-family: "Lato", sans-serif; position: relative; }

  .flyer {
    position: absolute; left: 31px; top: 196px;
    width: 1138px; height: 807px;
    background: var(--paper); overflow: hidden;
    box-shadow: 0 6px 24px rgba(0,0,0,.18);
  }
  .flyer__art { position: absolute; left: 0; top: 0; }

  .brand {
    position: absolute; left: 258px; top: 265px; width: 627px; height: 163px;
    display: flex; align-items: center; justify-content: center; gap: 14px;
    color: #ffffff; font-weight: 700; font-size: 36px;
  }
  .brand__dot { width: 18px; height: 18px; border-radius: 50%; background: #ffffff; }

  .step {
    position: absolute; top: 470px; width: 334px; height: 154px;
    display: flex; align-items: center; justify-content: center; text-align: center;
    color: var(--light-text); font-size: 24px; line-height: 30px; text-transform: uppercase;
    padding-top: 22px;
  }
  .step--apply { left: 24px; background: var(--blue); }
  .step--details { left: 402px; background: var(--orange); padding-top: 0; }
  .step--vehicle { left: 779px; background: var(--blue); }

  .step__badge {
    position: absolute; top: -33px; left: 50%; margin-left: -33px;
    width: 66px; height: 66px; border-radius: 50%;
    background: #ffffff; border: 2px solid var(--orange);
    display: flex; align-items: center; justify-content: center;
  }
  .step--details .step__badge { border-color: var(--blue); }

  .chevron { position: absolute; top: 530px; }

  .source-note {
    position: absolute; left: 24px; top: 650px;
    color: var(--muted); font-size: 23px; line-height: 30px;
  }

  .features {
    position: absolute; left: 778px; top: 632px; width: 337px; height: 101px;
    background: var(--panel); border-radius: 4px; padding: 6px 10px;
  }
  .feature {
    display: flex; align-items: center; gap: 12px; height: 44px;
    color: var(--ink); font-size: 23px;
  }
  .feature__icon {
    width: 38px; height: 38px; border-radius: 50%; background: #fff;
    border: 2px solid var(--orange); flex: none;
    display: flex; align-items: center; justify-content: center;
  }

  .call {
    position: absolute; left: 40px; top: 744px; height: 50px;
    display: flex; align-items: center; gap: 20px;
    color: #ffffff; font-weight: 900; font-size: 37px;
  }
  .web {
    position: absolute; left: 480px; top: 750px; width: 520px; text-align: center;
    color: #ffffff; font-size: 30px; letter-spacing: 5px;
  }
</style>
</head>
<body>
  <main class="flyer">
    <svg class="flyer__art" width="1138" height="807" viewBox="0 0 1138 807">
      <defs>
        <linearGradient id="carTone" x1="0" y1="0" x2="1" y2="1">
          <stop offset="0" stop-color="var(--photo-car-a)"/>
          <stop offset="1" stop-color="var(--photo-car-b)"/>
        </linearGradient>
        <linearGradient id="peopleTone" x1="0" y1="0" x2="1" y2="1">
          <stop offset="0" stop-color="var(--photo-people-a)"/>
          <stop offset="1" stop-color="var(--photo-people-b)"/>
        </linearGradient>
      </defs>
      <polygon role="img" aria-label="Photo of a white car front parked on a shaded dirt road"
        points="0,0 692,0 578,262 258,262 262,350 0,350" fill="url(#carTone)"/>
      <polygon role="img" aria-label="Photo of a smiling couple driving a car"
        points="700,0 1138,0 1138,358 852,358 888,262 586,262" fill="url(#peopleTone)"/>
      <polygon points="258,265 885,265 815,428 328,428" fill="var(--ink)"/>
      <polygon points="0,726 362,726 400,807 0,807" fill="var(--ink)"/>
      <polygon points="372,737 1138,737 1138,807 402,807" fill="var(--blue)"/>
    </svg>

    <div class="brand"><span class="brand__dot"></span>Clear Road Rentals</div>

    <section class="step step--apply">
      <span class="step__badge">
        <svg width="36" height="36" viewBox="0 0 36 36" fill="none" stroke="#444" stroke-width="2">
          <path d="M8 4h16v14M8 4v28h12"/><path d="M12 11h8M12 16h8M12 21h5"/><path d="M20 26l4 4 8-9" stroke="var(--orange)"/>
        </svg>
      </span>
      Apply online<br>or call<br>1800 452 817
    </section>

    <svg class="chevron" style="left:368px" width="24" height="32" viewBox="0 0 24 32"><path d="M2 2l18 14L2 30h8l12-14L10 2z" fill="var(--blue)"/></svg>

    <section class="step step--details">
      <span class="step__badge">
        <svg width="40" height="40" viewBox="0 0 40 40" fill="none" stroke="#444" stroke-width="2">
          <path d="M8 14c-2 2-2 6 2 11s9 8 12 7l3-3-5-4-2 2c-3-1-6-4-7-7l2-2-4-5z"/>
          <path d="M20 6a10 8 0 1 1 4 15l-4 3 1-4a10 8 0 0 1-1-14z" stroke="var(--blue)"/>
          <circle cx="25" cy="13" r=".8" fill="#444"/><circle cx="29" cy="13" r=".8" fill="#444"/><circle cx="33" cy="13" r=".8" fill="#444"/>
        </svg>
      </span>
      Provide accident<br>details
    </section>

    <svg class="chevron" style="left:745px" width="24" height="32" viewBox="0 0 24 32"><path d="M2 2l18 14L2 30h8l12-14L10 2z" fill="var(--orange)"/></svg>

    <section class="step step--vehicle">
      <span class="step__badge">
        <svg width="46" height="30" viewBox="0 0 46 30" fill="none" stroke="#444" stroke-width="2">
          <path d="M4 20v-6l6-2 5-7h16l5 7 6 2v6z"/><path d="M16 7l-3 5h20l-3-5z"/>
          <circle cx="13" cy="21" r="4" fill="#fff"/><circle cx="33" cy="21" r="4" fill="#fff"/>
        </svg>
      </span>
      You get a replacement<br>vehicle we<br>take care of the rest
    </section>

    <p class="source-note">Where you get this flyer from<br>when they call us</p>

    <ul class="features">
      <li class="feature">
        <span class="feature__icon">
          <svg width="24" height="16" viewBox="0 0 24 16" fill="none" stroke="#555" stroke-width="1.5"><path d="M2 2h13v10H2zM15 6h4l3 3v3h-7"/><circle cx="6" cy="13" r="2" fill="#fff"/><circle cx="18" cy="13" r="2" fill="#fff"/></svg>
        </span>
        Free Delivery
      </li>
      <li class="feature">
        <span class="feature__icon">
          <svg width="24" height="18" viewBox="0 0 24 18" fill="none" stroke="#555" stroke-width="1.5"><path d="M2 14v-4l3-1 3-4h9l3 4 2 1v4z"/><circle cx="7" cy="14" r="2" fill="#fff"/><circle cx="17" cy="14" r="2" fill="#fff"/></svg>
        </span>
        Late Model/ New Vehicle
      </li>
    </ul>

    <div class="call">
      <svg width="40" height="40" viewBox="0 0 40 40" fill="none" stroke="var(--orange)" stroke-width="3" stroke-linecap="round">
        <path d="M9 8c-4 3-3 9 3 16s13 10 17 7l2-3-6-5-3 2c-4-2-7-5-9-9l2-3-5-6z" fill="var(--orange)" stroke="none"/>
        <path d="M22 8a10 10 0 0 1 10 10M22 2a16 16 0 0 1 16 16"/>
      </svg>
      1800 452 817
    </div>
    <div class="web">www.clearroadrentals.com.au</div>
  </main>
</body>
</html>
```